National commercial insurance agency needs design for email campaign to other insurance agencies ...

National commercial insurance agency needs design for email campaign to other insurance agencies needing to place workers comp policies and and also need very intense risk management. We want to market to smaller insurance agencies to refer us to their larger clients or prospects.

Font styles to use
Sans Serif

```html
<!DOCTYPE html>
<html lang="en">
<head>
<meta charset="utf-8">
<title>Northline – Commercial Insurance Referral Campaign</title>
<link rel="stylesheet" href="https://fonts.googleapis.com/css2?family=Exo+2:wght@400;500;600;700&family=Noto+Serif:ital@1&display=swap">
<style>
  :root{
    --orange:#f26b35;
    --ink:#3a3a3a;
    --text:#555555;
    --muted:#777777;
    --line:#d8d8d8;
    --footer:#444444;
    --social:#3f7fc2;
    --white:#ffffff;
    --sans:"Exo 2", Arial, sans-serif;
    --serif:"Noto Serif", Georgia, serif;
  }
  *{box-sizing:border-box;margin:0;padding:0}
  html,body{width:1200px;height:4432px;overflow:hidden;background:var(--white)}
  body{position:relative;font-family:var(--sans);color:var(--text)}
  a{text-decoration:none}
  .abs{position:absolute}
  .photo{position:absolute}

  /* Brand name */
  .brand-name{font-family:var(--sans);font-weight:700;color:var(--white);letter-spacing:2px;white-space:nowrap}

  /* Hero */
  .hero{left:0;top:0;width:1200px;height:624px}
  .hero .brand-name{position:absolute;right:112px;top:50px;font-size:40px}
  .hero-title{position:absolute;left:84px;top:352px;font-size:42px;font-weight:400;color:var(--white);line-height:58px}
  .hero-title span{display:inline-block;background:rgba(40,40,40,.55);padding:0 10px}

  /* Feature band */
  .features{left:0;top:624px;width:1200px;height:282px;background:var(--orange);color:var(--white)}
  .feature{position:absolute;top:66px;width:245px}
  .feature h3{display:flex;align-items:center;gap:12px;font-size:23px;font-weight:600;margin-bottom:10px}
  .feature p{font-size:19px;line-height:28px}
  .feature svg{flex:none}

  /* Service rows */
  .service h2{font-size:33px;font-weight:500;color:var(--ink);margin-bottom:14px}
  .service p{font-size:25px;line-height:34px;color:var(--text)}
  .btn-outline{position:absolute;display:flex;align-items:center;justify-content:center;height:68px;border:3px solid var(--orange);font-size:24px;font-weight:500;color:var(--ink);background:var(--white)}
  .btn-solid{position:absolute;display:flex;align-items:center;justify-content:center;background:var(--orange);color:var(--white);font-weight:500}

  /* Referral band */
  .referral{left:0;top:1792px;width:1200px;height:390px}
  .referral p{position:absolute;left:0;top:92px;width:1200px;text-align:center;font-family:var(--serif);font-style:italic;font-size:32px;line-height:42px;color:var(--white)}

  /* Cards */
  .card{position:absolute;top:2230px;width:298px;height:484px;border:2px solid var(--line);background:var(--white)}
  .card .photo{left:0;top:0;width:100%;height:244px}
  .card h4{position:absolute;left:0;top:290px;width:100%;text-align:center;font-size:24px;font-weight:500;color:var(--ink);line-height:32px}
  .card .btn-outline{left:64px;top:396px;width:166px;height:54px;font-size:22px}

  /* Email draft */
  .draft{left:112px;top:2778px;width:979px;height:336px;border:3px solid var(--orange)}
  .draft h3{position:absolute;top:50px;width:100%;text-align:center;font-size:31px;font-weight:500;color:var(--ink)}
  .draft p{position:absolute;top:108px;left:85px;width:803px;text-align:center;font-size:24px;line-height:32px;color:var(--ink)}

  /* Closing card */
  .closing{left:112px;top:3178px;width:979px;height:694px;border:2px solid var(--line)}
  .closing .photo{left:0;top:0;width:100%;height:416px}
  .closing h3{position:absolute;top:456px;width:100%;text-align:center;font-size:31px;font-weight:600;color:var(--ink)}
  .closing p{position:absolute;top:510px;width:100%;text-align:center;font-size:24px;line-height:32px;font-weight:500;color:var(--ink)}

  /* Footer */
  .footer-bar{left:0;top:3936px;width:1200px;height:160px;background:var(--footer)}
  .footer-bar .brand-name{position:absolute;left:112px;top:52px;font-size:42px}
  .socials{position:absolute;right:112px;top:62px;display:flex;gap:14px}
  .socials span{width:40px;height:40px;border-radius:4px;background:var(--social)}
  .contact{left:112px;top:4140px;font-size:24px;line-height:38px;color:var(--ink);font-style:normal}
  .divider{left:112px;top:4310px;width:979px;height:2px;background:var(--ink)}
  .unsubscribe{right:109px;top:4340px;font-size:19px;color:var(--muted)}
</style>
</head>
<body>

<header class="abs hero">
  <div class="photo" role="img" aria-label="Photo of a bright modern retail store interior with shelves" style="left:0;top:0;width:1200px;height:624px;background:linear-gradient(160deg,#9a9da1 0%,#717478 50%,#505256 100%)"></div>
  <span class="brand-name">NORTHLINE</span>
  <h1 class="hero-title"><span>We offer a time tested personal</span><br><span>and analytical process for</span><br><span>commercial insurance solutions</span></h1>
</header>

<section class="abs features">
  <div class="feature" style="left:116px">
    <h3><svg width="22" height="24" viewBox="0 0 24 26"><circle cx="12" cy="7" r="6" fill="#fff"/><path d="M1 26c0-7 5-11 11-11s11 4 11 11z" fill="#fff"/></svg>COMPLIANCE</h3>
    <p>HR and safety onsite compliance.<br>Onsite training and programmes</p>
  </div>
  <div class="feature" style="left:458px">
    <h3><svg width="30" height="22" viewBox="0 0 32 24"><rect x="1.5" y="1.5" width="29" height="21" rx="2" fill="none" stroke="#fff" stroke-width="3"/><circle cx="16" cy="12" r="5" fill="#fff"/></svg>PROFIT LEAKS</h3>
    <p>Premium Recovery Audit.<br>We detect and correct profit leaks.<br>Incorrect class codes.</p>
  </div>
  <div class="feature" style="left:800px">
    <h3><svg width="22" height="26" viewBox="0 0 24 28"><path d="M2 1h14l6 6v20H2z" fill="#fff"/><path d="M6 12h12M6 17h12M6 22h8" stroke="#f26b35" stroke-width="2"/></svg>CLAIMS</h3>
    <p>Injury and claims management consulting.<br>We attend mediations on your behalf.</p>
  </div>
</section>

<section class="abs service" style="left:112px;top:978px;width:440px">
  <h2>HR Services</h2>
  <p>We can do it all - employment, compensation, benefits, employee relations, and training.</p>
</section>
<a class="btn-outline" style="left:112px;top:1184px;width:186px">More details</a>
<div class="photo" role="img" aria-label="Photo of a modern open-plan office with glass walls and desks" style="left:618px;top:982px;width:472px;height:320px;background:linear-gradient(135deg,#cfd2d3 0%,#8e9497 50%,#4e5559 100%)"></div>

<div class="photo" role="img" aria-label="Photo of two smiling warehouse workers in hard hats and blue overalls" style="left:112px;top:1376px;width:467px;height:320px;background:linear-gradient(135deg,#2f4d8a 0%,#3c62b0 45%,#d7b34a 100%)"></div>
<section class="abs service" style="left:618px;top:1366px;width:450px">
  <h2>Safety Complaince</h2>
  <p>We offer onsite training in English and Spanish. Discount safety equipment and drug test as low as $20 available.</p>
</section>
<a class="btn-outline" style="left:618px;top:1576px;width:186px">More details</a>

<section class="abs referral">
  <div class="photo" role="img" aria-label="Dark blurred photo of a person with warm bokeh lights" style="left:0;top:0;width:1200px;height:390px;background:radial-gradient(circle at 85% 70%,#6b5a44 0%,#4a4a4a 40%,#3a3a3a 100%)"></div>
  <p>We kndly request you to refer to us your larger<br>clients or prospects. Please follow link to<br>discuss the commission.</p>
  <a class="btn-solid" style="left:502px;top:266px;width:212px;height:54px;font-size:23px">More details</a>
</section>

<article class="card" style="left:112px">
  <div class="photo" role="img" aria-label="Photo of a worker in a hard hat handling materials" style="background:linear-gradient(135deg,#c9a24a 0%,#3d5b8f 60%,#27384f 100%)"></div>
  <h4>Risk Management<br>Centre</h4>
  <a class="btn-outline">More details</a>
</article>
<article class="card" style="left:451px">
  <div class="photo" role="img" aria-label="Photo of two people meeting in a bright lounge" style="background:linear-gradient(135deg,#e4e6e4 0%,#b7c2bf 55%,#8a9592 100%)"></div>
  <h4>Work Comp<br>Re-audit Services</h4>
  <a class="btn-outline">More details</a>
</article>
<article class="card" style="left:792px">
  <div class="photo" role="img" aria-label="Photo of a welder in a protective mask with sparks" style="background:linear-gradient(135deg,#2e3d63 0%,#4f6aa3 55%,#d9b35c 100%)"></div>
  <h4>Premium<br>Recovery</h4>
  <a class="btn-outline">More details</a>
</article>

<section class="abs draft">
  <h3>ALREADY MADE EMAIL DRAFT</h3>
  <p>Follow this link for an already made email. You only need to input the names of the clients. Alternatively you can make your own email according to your preference.</p>
  <a class="btn-solid" style="left:394px;top:226px;width:186px;height:64px;font-size:28px">Email</a>
</section>

<section class="abs closing">
  <div class="photo" role="img" aria-label="Photo looking up at glass skyscrapers against a cloudy sky" style="background:linear-gradient(180deg,#c7cdd3 0%,#7d858d 45%,#2f353b 100%)"></div>
  <h3>NORTHLINE is the answer when it comes to Work Comp</h3>
  <p>Is your company in compliance? Is your experience mode correct?<br>Do you have an out of control claim?</p>
  <a class="btn-outline" style="left:402px;top:598px;width:170px;height:54px;font-size:22px">More details</a>
</section>

<footer>
  <div class="abs footer-bar">
    <span class="brand-name">NORTHLINE</span>
    <div class="socials" aria-label="Social links"><span></span><span></span><span></span></div>
  </div>
  <address class="abs contact">Contact Us<br>48 Harlow Ave, Suite 5, Brookfield, FL 33900<br>(555) 014 2270</address>
  <div class="abs divider"></div>
  <a class="abs unsubscribe">unsubscribe</a>
</footer>

</body>
</html>
```